Business Cards Design for the electrical wholesaler: clean bold dynamic :)

We need a business card design that would follow our latest brand guidelines. As an electrical wholesaler we want to bring a fresh look and feel into the industry. The design should be clean bold and dynamic. It should come alive with the renewed energy of our green colour. Our grey colour should keep things balanced and complement the notion of maturity and responsibility. We employ Lato as a corporate font however are not bound by this font and we’re open to interpretation here.

Target Market(s)

Electrical contractors

Industry/Entity Type

Business

Contact Information for Business Card

Logo
Name & Surname: Olesia Hrybenko
Job Title: Director of Marketing
Email: olesia.hrybenko@mailvex.com
Cell phone: XXX.XXX.XXXX
Address: 20517 - 88 Ave. Edmonton, AB, Canada. T6K 2N8
Business Phone: 780.362.7048
Website: www.kopra.ca

Font styles to use
Other font styles liked:
• Lato

Requirements
Must have
• Logo & website
Nice to have
• Brand elements - some of them you may find in the attached Brand Guidelines (e.g. three lines on the background signifying "W")

```html
<!DOCTYPE html>
<html lang="en">
<head>
<meta charset="utf-8">
<title>Kopra Business Card</title>
<link href="https://fonts.googleapis.com/css2?family=Lato:wght@300;400;700&display=swap" rel="stylesheet">
<style>
  :root {
    --backdrop: #a2d1ac;
    --slate: #2e3338;
    --slate-deep: #22262a;
    --slate-light: #3b4147;
    --brand-green: #5cb85f;
    --paper: #f7f7f5;
    --paper-shade: #e9ecea;
    --ink: #1f2326;
    --muted: #5d6368;
  }
  * { margin: 0; padding: 0; box-sizing: border-box; }
  html, body {
    width: 1200px; height: 900px; overflow: hidden;
    background: var(--backdrop);
    font-family: "Lato", sans-serif;
  }
  .canvas { position: relative; width: 1200px; height: 900px; }

  .card {
    position: absolute; left: 240px;
    width: 720px; height: 412px;
    overflow: hidden;
    box-shadow: 0 10px 24px rgba(20, 50, 30, 0.22);
  }
  .card--back { top: 28px; background: var(--slate); }
  .card--front { top: 462px; display: flex; }

  .surface-pattern {
    position: absolute; inset: 0;
    background:
      radial-gradient(ellipse at 50% 50%, var(--slate-light) 0%, var(--slate) 55%, var(--slate-deep) 100%);
  }
  .brand-frame {
    position: absolute; inset: 18px;
    border: 1.5px solid var(--brand-green);
  }

  .wordmark {
    position: absolute; left: 50%; top: 50%;
    transform: translate(-50%, -50%);
    display: flex; align-items: center; gap: 14px;
    color: var(--brand-green);
    white-space: nowrap;
  }
  .wordmark__dot {
    flex: none; width: 46px; height: 46px; border-radius: 50%;
    background: var(--brand-green);
  }
  .wordmark__name {
    display: block; font-weight: 700; font-size: 64px; line-height: 1;
  }
  .wordmark__tagline {
    display: block; font-weight: 400; font-size: 11px;
    letter-spacing: 2.4px; text-transform: uppercase; margin-top: 6px;
  }

  .front-brand {
    position: relative; width: 52%; height: 100%;
    background: var(--slate);
  }
  .front-brand .wordmark__name { font-size: 58px; }
  .front-brand .wordmark__dot { width: 40px; height: 40px; }

  .front-details {
    position: relative; width: 48%; height: 100%;
    background: var(--paper);
    padding: 80px 24px 0 44px;
    color: var(--ink);
  }
  .front-details .surface-pattern {
    background: linear-gradient(135deg, var(--paper) 0%, var(--paper-shade) 100%);
  }
  .contact { position: relative; }
  .contact__name {
    font-weight: 400; font-size: 25px; line-height: 1.15;
    text-transform: uppercase; letter-spacing: 0.5px;
  }
  .contact__title {
    font-weight: 300; font-size: 14px; letter-spacing: 2.6px;
    color: var(--muted); margin-top: 3px;
  }
  .contact__list { list-style: none; margin-top: 22px; }
  .contact__item {
    display: flex; align-items: flex-start; gap: 12px;
    font-size: 12.5px; line-height: 1.35; margin-bottom: 9px;
  }
  .contact__icon {
    width: 14px; height: 14px; flex: none; margin-top: 1px;
    fill: var(--ink);
  }
  .contact__icon--line { fill: none; stroke: var(--ink); stroke-width: 2; }
</style>
</head>
<body>
<main class="canvas">

  <section class="card card--back" aria-label="Card back">
    <div class="surface-pattern" role="img" aria-label="Faint geometric line pattern on dark grey"></div>
    <div class="brand-frame"></div>
    <div class="wordmark">
      <span class="wordmark__dot"></span>
      <div>
        <span class="wordmark__name">kopra</span>
        <span class="wordmark__tagline">Electrical Wholesalers</span>
      </div>
    </div>
  </section>

  <section class="card card--front" aria-label="Card front">
    <div class="front-brand">
      <div class="surface-pattern" role="img" aria-label="Faint geometric line pattern on dark grey"></div>
      <div class="wordmark">
        <span class="wordmark__dot"></span>
        <span class="wordmark__name">kopra</span>
      </div>
    </div>

    <div class="front-details">
      <div class="surface-pattern" role="img" aria-label="Faint green geometric line pattern on white"></div>
      <div class="contact">
        <h1 class="contact__name">Olesia Hrybenko</h1>
        <p class="contact__title">Director of Marketing</p>
        <ul class="contact__list">
          <li class="contact__item">
            <svg class="contact__icon" viewBox="0 0 24 24"><path d="M12 2a7 7 0 0 0-7 7c0 5 7 13 7 13s7-8 7-13a7 7 0 0 0-7-7zm0 9.5A2.5 2.5 0 1 1 12 6.5a2.5 2.5 0 0 1 0 5z"/></svg>
            <span>20517 - 88 Ave. Edmonton<br>AB, Canada. T6K 2N8</span>
          </li>
          <li class="contact__item">
            <svg class="contact__icon contact__icon--line" viewBox="0 0 24 24"><path d="M2 6h20v12H2z M2 6l10 7 10-7"/></svg>
            <span>olesia.hrybenko@mailvex.com</span>
          </li>
          <li class="contact__item">
            <svg class="contact__icon contact__icon--line" viewBox="0 0 24 24"><rect x="7" y="3" width="10" height="18" rx="2"/><path d="M11 18h2"/></svg>
            <span>XXX.XXX.XXXX</span>
          </li>
          <li class="contact__item">
            <svg class="contact__icon" viewBox="0 0 24 24"><path d="M6.6 10.8a15 15 0 0 0 6.6 6.6l2.2-2.2a1 1 0 0 1 1-.25 11.4 11.4 0 0 0 3.6.57 1 1 0 0 1 1 1V20a1 1 0 0 1-1 1A17 17 0 0 1 3 4a1 1 0 0 1 1-1h3.5a1 1 0 0 1 1 1c0 1.25.2 2.45.57 3.6a1 1 0 0 1-.25 1z"/></svg>
            <span>780.362.7048</span>
          </li>
          <li class="contact__item">
            <svg class="contact__icon contact__icon--line" viewBox="0 0 24 24"><circle cx="12" cy="12" r="9.5"/><path d="M2.5 12h19M12 2.5c3 3 3 16 0 19M12 2.5c-3 3-3 16 0 19" stroke-width="1.6"/></svg>
            <span>www.kopra.ca</span>
          </li>
        </ul>
      </div>
    </div>
  </section>

</main>
</body>
</html>
```